Stationery Design Project - New innovative law firm

I need a simple design, yet the tone of the stationery set need to express modern, professionalism, smart and forward-thinking. I don’t need a business card, but require the stationery set to have:
• Design letterhead
• Design facsimile
• Design memo
The triangular logo with Corvane Associates words etc, need to be present in the stationery. The red triangular logo should not be re-designed, but feel free to play around with the placement and colours of the Corvane Associates words etc....?

Target Market(s)

Business clients

Industry/Entity Type

Business

Requirements
Must have
• The triangular logo with Corvane Associates words etc...for branding.

```html
<!DOCTYPE html>
<html lang="en">
<head>
<meta charset="utf-8">
<title>Corvane Associates – Memo</title>
<link rel="stylesheet" href="https://fonts.googleapis.com/css2?family=Open+Sans:wght@400;600;700&display=swap">
<style>
  :root {
    --backdrop: #cfcfcf;
    --paper: #ffffff;
    --ink-dark: #1f1f1f;
    --ink-grey: #6e6e6e;
    --ink-soft: #555555;
    --rule: #8a8a8a;
    --brand-red: #e31e24;
    --band-dark: #2b2b2b;
  }
  * { box-sizing: border-box; margin: 0; padding: 0; }
  html, body {
    width: 1200px; height: 900px; overflow: hidden;
    background: var(--backdrop);
    font-family: "Open Sans", Arial, sans-serif;
  }
  .memo-sheet {
    position: absolute; left: 300px; top: 26px;
    width: 600px; height: 848px;
    background: var(--paper);
    box-shadow: 0 4px 18px rgba(0,0,0,.18);
    overflow: hidden;
  }
  .brand {
    position: absolute; left: 78px; top: 76px;
  }
  .brand-row { display: flex; align-items: center; gap: 10px; }
  .brand-mark { width: 34px; height: 34px; background: var(--brand-red); }
  .brand-name {
    font-weight: 700; font-size: 22px; letter-spacing: .5px;
    color: var(--ink-dark); text-transform: uppercase; line-height: 1;
  }
  .brand-tagline {
    margin: 4px 0 0 44px;
    font-size: 8.5px; letter-spacing: .3px; color: var(--ink-soft);
    text-transform: uppercase;
  }
  .memo-title {
    position: absolute; left: 78px; top: 166px;
    font-size: 34px; font-weight: 400; color: var(--ink-grey);
  }
  .memo-fields {
    position: absolute; left: 84px; top: 280px; width: 260px;
    list-style: none;
  }
  .memo-field {
    display: flex; align-items: flex-end; gap: 8px;
    height: 26px; font-size: 11px; color: var(--ink-soft);
  }
  .memo-field .field-line {
    flex: 1; border-bottom: 1px solid var(--rule); margin-bottom: 3px;
  }
  .memo-field.comments { margin-top: 2px; }
  .contact {
    position: absolute; right: 22px; bottom: 42px;
    text-align: right; font-size: 10.5px; line-height: 1.35; color: var(--ink-soft);
  }
  .contact .label { color: var(--brand-red); font-weight: 600; }
  .contact p + p { margin-top: 6px; }
  .footer-band {
    position: absolute; left: 0; right: 0; bottom: 0; height: 22px;
    background: var(--band-dark);
  }
  .footer-web {
    position: absolute; right: 0; bottom: 0; height: 22px; width: 200px;
    background: var(--brand-red);
    clip-path: polygon(8px 0, 100% 0, 100% 100%, 0 100%);
    color: #fff; font-size: 11px; line-height: 22px; padding-left: 22px;
  }
  .footer-web strong { font-weight: 700; }
</style>
</head>
<body>
  <main class="memo-sheet">
    <header class="brand">
      <div class="brand-row">
        <span class="brand-mark" aria-hidden="true"></span>
        <span class="brand-name">Corvane Associates</span>
      </div>
      <p class="brand-tagline">Accounting, Tax, Business Advice &amp; Legal</p>
    </header>

    <h1 class="memo-title">memo</h1>

    <ul class="memo-fields">
      <li class="memo-field"><span>To</span><span class="field-line"></span></li>
      <li class="memo-field"><span>From</span><span class="field-line"></span></li>
      <li class="memo-field"><span>CC</span><span class="field-line"></span></li>
      <li class="memo-field"><span>Date</span><span class="field-line"></span></li>
      <li class="memo-field"><span>Re</span><span class="field-line"></span></li>
      <li class="memo-field comments"><span>Comments:</span><span class="field-line"></span></li>
    </ul>

    <address class="contact" style="font-style:normal">
      <p><span class="label">Address:</span><br>Unit 4/12 Halden Rd,<br>Northmere, NSW 2199</p>
      <p><span class="label">Ph:</span> +61 2 5550 1234<br><span class="label">Mob:</span> +61 400 555 012</p>
      <p><span class="label">E:</span>admin@corvane-associates.com.au</p>
    </address>

    <footer class="footer-band">
      <div class="footer-web">www.<strong>corvaneassociates</strong>.com.au</div>
    </footer>
  </main>
</body>
</html>
```